Business cards design on a high standard

We advise clients on insurance and financial matters, since these clients pay for our advice, the design should have a high standard. Our logo should be included. From the colors we are open for everything.

Colors

Designer to choose colors to be used in the design.

```html
<!DOCTYPE html>
<html lang="en">
<head>
<meta charset="utf-8">
<title>Alpen Counsel – Business Cards</title>
<link href="https://fonts.googleapis.com/css2?family=Roboto:wght@400;500;700&display=swap" rel="stylesheet">
<style>
  :root {
    --backdrop: #2a2624;
    --card: #2e2e30;
    --card-edge: #e0242c;
    --accent: #e0242c;
    --ink: #f2f2f2;
    --ink-soft: #d9d9d9;
    --emboss: #3a3a3d;
    --divider: #e6e6e6;
  }
  * { margin: 0; padding: 0; box-sizing: border-box; }
  html, body { width: 1200px; height: 716px; overflow: hidden; }
  body {
    background: var(--backdrop);
    font-family: "Roboto", Arial, sans-serif;
    position: relative;
  }
  .card {
    position: absolute;
    top: 203px;
    width: 540px;
    height: 310px;
    background: var(--card);
    border: 2px solid var(--card-edge);
    box-shadow: 0 14px 30px rgba(0,0,0,0.45);
  }
  .card--front { left: 40px; }
  .card--back  { left: 620px; }

  .brand {
    display: flex;
    align-items: center;
    gap: 12px;
    font-weight: 700;
    text-transform: uppercase;
    letter-spacing: 0.04em;
    line-height: 1;
    white-space: nowrap;
  }
  .brand__dot { border-radius: 50%; flex: none; }

  .card--front .brand {
    position: absolute;
    left: 50%; top: 50%;
    transform: translate(-50%, -50%);
    font-size: 46px;
    color: var(--emboss);
  }
  .card--front .brand__dot { width: 30px; height: 30px; background: var(--emboss); }

  .card--back .brand {
    position: absolute;
    left: 28px; top: 142px;
    gap: 10px;
    font-size: 22px;
    color: var(--accent);
  }
  .card--back .brand__dot { width: 16px; height: 16px; background: var(--accent); }

  .divider {
    position: absolute;
    left: 274px; top: 82px;
    width: 1px; height: 150px;
    background: var(--divider);
  }
  .contact {
    position: absolute;
    left: 298px; top: 84px;
    color: var(--ink);
  }
  .contact__name {
    color: var(--accent);
    font-size: 19px;
    font-weight: 500;
    letter-spacing: 0.02em;
    text-transform: uppercase;
  }
  .contact__role { font-size: 14px; margin-top: 4px; color: var(--ink-soft); }
  .contact__address { font-size: 13px; margin-top: 12px; line-height: 1.4; color: var(--ink-soft); }
  .contact__list { list-style: none; margin-top: 12px; font-size: 13px; }
  .contact__list li { display: flex; align-items: center; gap: 8px; margin-top: 4px; }
  .contact__list svg { width: 12px; height: 12px; fill: var(--accent); flex: none; }
  .highlight { color: var(--accent); }
</style>
</head>
<body>
  <section class="card card--front" aria-label="Card front">
    <div class="brand"><span class="brand__dot"></span>Alpen Counsel</div>
  </section>

  <section class="card card--back" aria-label="Card back">
    <div class="brand"><span class="brand__dot"></span>Alpen Counsel</div>
    <div class="divider"></div>
    <div class="contact">
      <p class="contact__name">Daniel Carter</p>
      <p class="contact__role">Manager</p>
      <p class="contact__address">Your address, city<br>state, ZIP 0000</p>
      <ul class="contact__list">
        <li><svg viewBox="0 0 24 24" aria-hidden="true"><path d="M6.6 10.8a15 15 0 0 0 6.6 6.6l2.2-2.2a1 1 0 0 1 1-.25 11.4 11.4 0 0 0 3.6.57 1 1 0 0 1 1 1V20a1 1 0 0 1-1 1A17 17 0 0 1 3 4a1 1 0 0 1 1-1h3.5a1 1 0 0 1 1 1c0 1.25.2 2.45.57 3.57a1 1 0 0 1-.25 1z"/></svg><span>123-456-2100</span></li>
        <li><svg viewBox="0 0 24 24" aria-hidden="true"><path d="M2 5h20v14H2z M2 5l10 8 10-8" /></svg><span>youremail@mailbox.com</span></li>
        <li><svg viewBox="0 0 24 24" aria-hidden="true"><circle cx="12" cy="12" r="10"/></svg><span>www.<span class="highlight">yourwebsite</span>.com</span></li>
      </ul>
    </div>
  </section>
</body>
</html>
```